Corporate flyer highlighting service offering for PR agency

A corporate flyer is needed for a new service offering that we are doing. The product name is HarborLeap it is a marketing and communications services offering for companies who are getting ready to sell their business. If we are really happy with the designer's work, there will be a great deal more projects. I am looking for a clean design with a few pops of color from my site. https://quillmarsh.partners. I am looking for a good design with data in sections. I am looking for a clean design that feels high-end but not cluttered. Please do not use images of people. Please see the following examples of types of designs I like.
https://www.tackboard.example/pin/839201746530918264/
https://www.tackboard.example/pin/402918375561029847/
https://assets.stockvale.example/corporate-flyer-template-KRTPMB
https://designbrook.example/item/corporate-flyer-template/81046395?s_rank=8
https://assets.stockvale.example/corporate-business-flyer-template-93PX7D

I had to place the project on hold as I choose the wrong type of project and did not get many designs as a result. I am reposting this with an updated brief.

Target Market(s)

Business sellers and brokers

Industry/Entity Type

Marketing for business sellers

Font styles to use
Sans Serif

Requirements
Must have
• Good quality design with content in sections. Clean and high end feeling is a must.
Should not have
• A lot of images of people.

```html
<!DOCTYPE html>
<html lang="en">
<head>
<meta charset="utf-8">
<title>HarborLeap Flyer – Quillmarsh Partners</title>
<link href="https://fonts.googleapis.com/css2?family=Poppins:wght@400;500;600;700&display=swap" rel="stylesheet">
<style>
:root{
  --navy:#0f1f2c;
  --navy-2:#16293a;
  --blue:#2a8fd0;
  --teal:#1995c2;
  --green:#5aa43c;
  --orange:#f5a01f;
  --red:#f05a24;
  --ink:#2a2f36;
  --paper:#ffffff;
}
*{margin:0;padding:0;box-sizing:border-box}
html,body{width:916px;height:1200px;overflow:hidden;background:#fff}
body{position:relative;font-family:'Poppins',sans-serif;color:var(--ink)}
.page{position:absolute;width:354px;height:500px;background:var(--paper);overflow:hidden;box-shadow:0 6px 14px rgba(0,0,0,.18)}
.page-1{left:74px;top:74px}
.page-2{left:490px;top:74px}
.page-3{left:74px;top:623px}
.page-4{left:486px;top:623px}
.abs{position:absolute}
.copy{position:absolute;font-size:5.7px;line-height:8.3px;text-align:justify;color:var(--ink)}
.copy b{font-weight:600}
.hero{position:absolute;left:0;top:0;width:354px;background:linear-gradient(135deg,var(--navy-2),var(--navy))}
.hero-text{position:absolute;color:#fff;font-size:6.4px;line-height:8.3px;text-align:justify}
.brand{position:absolute;text-align:center;color:#fff;font-weight:600;letter-spacing:.5px}
.brand .name{display:block;font-size:15.5px;line-height:18px}
.brand .sub{display:block;font-size:7px;letter-spacing:3px;line-height:10px}
.footer-bar{position:absolute;left:0;bottom:0;width:354px;height:6px;background:var(--navy)}
.footer-url{position:absolute;left:19px;bottom:6px;font-size:4.6px;line-height:7px;font-weight:500;color:var(--navy);background:#fff;padding-right:6px}
.quote-box{position:absolute;border:1px solid #333;padding:5px 8px;font-size:5.7px;line-height:8px;color:var(--ink)}
.service-row{position:absolute;left:0;top:327px;width:354px;height:60px}
.service{position:absolute;width:60px;text-align:center;font-size:5.4px;line-height:7.6px;font-weight:600;text-transform:uppercase}
.service svg{display:block;margin:0 auto 2px}
.tab{position:absolute;left:0;height:10px;background:var(--blue);color:#fff;font-size:5.4px;line-height:10px;font-weight:600;padding-left:19px;clip-path:polygon(0 0,calc(100% - 5px) 0,100% 50%,calc(100% - 5px) 100%,0 100%)}
.bullets{position:absolute;list-style:none;font-size:5.7px;line-height:8.3px}
.bullets li{position:relative;padding-left:11px;margin-bottom:8.3px;text-align:justify}
.bullets li::before{content:"";position:absolute;left:0;top:2.5px;width:3.4px;height:3.4px;border-radius:50%;background:var(--c)}
.bullets .lead{color:var(--c);font-weight:500}
.stat{position:absolute;font-size:5.7px;line-height:8.3px;color:var(--ink)}
.cite{position:absolute;font-size:3.9px;line-height:5px;color:var(--ink);white-space:nowrap}
.checks{position:absolute;list-style:none;font-size:5.7px;line-height:7px}
.checks li{position:relative;padding-left:11px;margin-bottom:3px}
.checks li::before{content:"";position:absolute;left:1px;top:1px;width:2.6px;height:4.4px;border:solid var(--navy);border-width:0 1px 1px 0;transform:rotate(40deg)}
.dots{position:absolute;list-style:none;font-size:5.7px;line-height:7px}
.dots li{position:relative;padding-left:11px;margin-bottom:3px}
.dots li::before{content:"";position:absolute;left:1px;top:2px;width:3px;height:3px;border-radius:50%;background:var(--navy)}
.media-item{position:absolute;font-size:5.7px;line-height:7px;padding-left:15px;width:155px}
.media-item::before{content:"";position:absolute;left:0;top:0;width:11px;height:11px;border-radius:50%;background:#555a60}
.review-box{position:absolute;border:1.2px solid var(--blue);font-size:5.7px;line-height:8.3px;text-align:center;padding:8px 8px 0}
.review-title{position:absolute;left:50%;top:-5px;transform:translateX(-50%);background:#fff;padding:0 4px;color:var(--blue);font-size:5.6px;font-weight:600;white-space:nowrap;line-height:9px}
.stars{position:absolute;left:50%;bottom:-5px;transform:translateX(-50%);background:#fff;padding:0 4px;color:var(--blue);font-size:8px;line-height:9px;letter-spacing:1px}
.photo{position:absolute}
.quote-frame{position:absolute;border:1px solid rgba(255,255,255,.75)}
.quote-line{position:absolute;color:#fff;font-weight:600;text-transform:uppercase;text-align:center;font-size:7.6px;line-height:10px}
.quote-by{position:absolute;color:#fff;font-weight:600;font-size:8px;line-height:10px;text-align:center}
.deliverable{position:absolute;font-size:5.7px;line-height:8.3px;text-align:justify}
.deliverable .lead{color:var(--blue);font-weight:600}
.deliverable-icon{position:absolute;width:13px;height:13px;border-radius:50%;border:1px solid var(--blue)}
.brand-dark{position:absolute;text-align:center;color:var(--navy);font-weight:600}
.brand-dark .name{display:block;font-size:15px;line-height:18px;letter-spacing:.5px}
.brand-dark .sub{display:block;font-size:7px;letter-spacing:3px;line-height:10px}
</style>
</head>
<body>

<section class="page page-1">
  <div class="hero" style="height:162px"></div>
  <svg class="photo" width="354" height="162" viewBox="0 0 354 162" role="img" aria-label="City skyline photograph seen from above">
    <defs>
      <linearGradient id="skyline" x1="0" y1="0" x2="0" y2="1">
        <stop offset="0" stop-color="#9cc2dd"/>
        <stop offset=".5" stop-color="#6d92a8"/>
        <stop offset=".55" stop-color="#6fa24a"/>
        <stop offset="1" stop-color="#4d7a34"/>
      </linearGradient>
    </defs>
    <polygon points="213,0 354,0 354,162 207,162 253,78" fill="url(#skyline)"/>
    <polyline points="207,0 246,78 200,162" fill="none" stroke="#fff" stroke-width="1"/>
    <polygon points="224,41 245,78 202,78" fill="#f5a01f"/>
    <polygon points="202,78 245,78 224,114" fill="#f05a24"/>
  </svg>
  <div class="brand" style="left:25px;top:66px;width:152px">
    <span class="name">QUILLMARSH</span>
    <span class="sub">PARTNERS</span>
  </div>
  <p class="hero-text" style="left:25px;top:98px;width:150px">HarborLeap provides executives and business owners with clear guidance to unlock non-financial value ahead of an exit.</p>

  <p class="copy" style="left:19px;top:169px;width:316px">A strong communication and marketing strategy can significantly increase the value of your business leading up to an exit. Buyers are looking to mitigate risk and unlock potential value as a catalyst for clear growth potential.</p>
  <p class="copy" style="left:19px;top:201px;width:316px">Highlighting your company's success in the marketplace, identifying, and mitigating reptation risks before buyers do, enhancing employee engagement, finding hidden opportunities to boost marketing KPIs and showcasing IP, data, and innovation, can make a significant difference in valuation.</p>
  <div class="quote-box" style="left:33px;top:234px;width:280px;height:47px">US institutional investors believe that Investor Relations (IR) accounts for a total variance of <b>30%</b> in a company's valuation – from a premium of <b>10%</b> for "superb" IR to a discount of <b>20%</b> for "poor" IR. <b>---Corvane Research Group, "Harnessing IR's Power to Impact a Company's Valuation."</b></div>
  <p class="copy" style="left:19px;top:293px;width:316px">We design and implement communication and marketing strategies that deliver significant increases in brand awareness, identify reputational risks, and enhance brand perception, helping owners and investors to realize premium values for their companies. We support owners and companies through:</p>

  <div class="service-row">
    <div class="service" style="left:11px;color:var(--blue)">
      <svg width="44" height="38" viewBox="0 0 44 38"><polygon points="11,2 33,2 42,19 33,36 11,36 2,19" fill="none" stroke="var(--blue)" stroke-width="2.5"/><path d="M15 26V17l7-5 7 5v9z" fill="none" stroke="var(--blue)" stroke-width="1.2"/><rect x="20" y="20" width="4" height="6" fill="none" stroke="var(--blue)" stroke-width="1"/></svg>
      Company Exit<br>Preparation
    </div>
    <div class="service" style="left:76px;color:var(--teal)">
      <svg width="44" height="38" viewBox="0 0 44 38"><polygon points="11,2 33,2 42,19 33,36 11,36 2,19" fill="none" stroke="var(--teal)" stroke-width="2.5"/><rect x="14" y="17" width="7" height="9" fill="none" stroke="var(--teal)" stroke-width="1.1"/><rect x="23" y="11" width="8" height="15" fill="none" stroke="var(--teal)" stroke-width="1.1"/></svg>
      M &amp; A
    </div>
    <div class="service" style="left:144px;color:var(--green)">
      <svg width="44" height="38" viewBox="0 0 44 38"><polygon points="11,2 33,2 42,19 33,36 11,36 2,19" fill="none" stroke="var(--green)" stroke-width="2.5"/><polyline points="13,26 18,20 23,23 30,13" fill="none" stroke="var(--green)" stroke-width="1.2"/><line x1="13" y1="28" x2="31" y2="28" stroke="var(--green)" stroke-width="1.1"/></svg>
      IPO
    </div>
    <div class="service" style="left:211px;color:var(--red)">
      <svg width="44" height="38" viewBox="0 0 44 38"><polygon points="11,2 33,2 42,19 33,36 11,36 2,19" fill="none" stroke="var(--red)" stroke-width="2.5"/><circle cx="19" cy="20" r="5" fill="none" stroke="var(--red)" stroke-width="1.2"/><rect x="25" y="18" width="6" height="9" fill="none" stroke="var(--red)" stroke-width="1.1"/></svg>
      Spinoff<br>/Divestiture
    </div>
    <div class="service" style="left:279px;color:var(--orange)">
      <svg width="44" height="38" viewBox="0 0 44 38"><polygon points="11,2 33,2 42,19 33,36 11,36 2,19" fill="none" stroke="var(--orange)" stroke-width="2.5"/><circle cx="22" cy="15" r="4" fill="none" stroke="var(--orange)" stroke-width="1.2"/><path d="M14 28c1-6 15-6 16 0" fill="none" stroke="var(--orange)" stroke-width="1.2"/></svg>
      New Leadership<br>/Investor
    </div>
  </div>

  <p class="copy" style="left:19px;top:396px;width:316px">Few sellers would list their home without first inspecting, repairing broken items, and making updates to highlight the positive aspects --increasing appeal to buyers. However, countless business owners leave money on the table during corporate exits due to a lack of preparation.</p>
  <p class="copy" style="left:19px;top:428px;width:316px">Our team of executive-level communications and marketing experts brings deep buy and sell-side experience. We have played critical roles in the acquisition, integration, and disposition process. Our mix of financial services expertise combined with decades of experience leading internal and external communications, marketing and investor relations teams gives us a unique perspective on identifying and unlocking non-financial areas of value and mitigating non-financial risks before exit.</p>

  <div class="footer-bar"></div>
  <div class="footer-url">WWW.QUILLMARSH.PARTNERS.COM</div>
</section>

<section class="page page-2">
  <div class="hero" style="height:104px"></div>
  <svg class="photo" width="354" height="104" viewBox="0 0 354 104" role="img" aria-label="Photograph of a desk with a laptop in blue light">
    <defs>
      <linearGradient id="deskphoto" x1="0" y1="0" x2="1" y2="1">
        <stop offset="0" stop-color="#3d6fa6"/>
        <stop offset="1" stop-color="#1c3a63"/>
      </linearGradient>
    </defs>
    <polygon points="229,0 354,0 354,104 240,104 205,52" fill="url(#deskphoto)"/>
    <polyline points="222,0 198,52 232,104" fill="none" stroke="#fff" stroke-width="1"/>
  </svg>
  <p class="hero-text" style="left:20px;top:19px;width:166px">While accounting and investment banking teams are hard at work increasing value from a financial perspective, we help organizations enhance their valuation by identifying areas that will appeal most to buyers and ensuring those elements of your business are visible and memorable to those who matter most.</p>

  <svg class="abs" style="left:0;top:110px" width="354" height="110" viewBox="0 0 354 110">
    <g fill="var(--teal)"><polygon points="22,12 110,12 118,27 110,42 22,42 14,27"/></g>
    <polygon points="22,70 110,70 118,86 110,102 22,102 14,86" fill="var(--red)"/>
    <polygon points="240,12 330,12 338,27 330,42 240,42 232,27" fill="var(--green)"/>
    <polygon points="240,70 337,70 345,86 337,102 240,102 232,86" fill="var(--orange)"/>
    <g font-family="Poppins, sans-serif" font-size="5.6" fill="#fff" text-anchor="middle">
      <text x="66" y="29">Highlighting value in a</text><text x="66" y="36">clear &amp; visible way.</text>
      <text x="66" y="92">Streamlining the exit process.</text>
      <text x="285" y="29">Identifying potential risks &amp;</text><text x="285" y="36">suggesting mitigation measures.</text>
      <text x="288" y="91">Creating a polished presence in the</text><text x="288" y="98">market ahead of buyer interest.</text>
    </g>
    <g fill="#fff" stroke-width="1.8">
      <polygon points="61,2 71,2 76,10 71,18 61,18 56,10" stroke="var(--teal)"/>
      <polygon points="61,60 71,60 76,68 71,76 61,76 56,68" stroke="var(--red)"/>
      <polygon points="280,2 290,2 295,10 290,18 280,18 275,10" stroke="var(--green)"/>
      <polygon points="283,60 293,60 298,68 293,76 283,76 278,68" stroke="var(--orange)"/>
    </g>
    <g fill="none" stroke-width=".9">
      <ellipse cx="66" cy="10" rx="3.5" ry="2.2" stroke="var(--teal)"/>
      <circle cx="66" cy="68" r="2.8" stroke="var(--red)"/>
      <polygon points="285,6.5 288.5,13 281.5,13" stroke="var(--green)"/>
      <rect x="285" y="65" width="6" height="6" stroke="var(--orange)"/>
    </g>
    <g stroke="var(--navy)" stroke-width=".7" fill="var(--navy)">
      <line x1="123" y1="19" x2="140" y2="24"/><circle cx="123" cy="19" r="1.2"/>
      <line x1="123" y1="93" x2="140" y2="82"/><circle cx="123" cy="93" r="1.2"/>
      <line x1="227" y1="18" x2="212" y2="24"/><circle cx="227" cy="18" r="1.2"/>
      <line x1="228" y1="95" x2="214" y2="83"/><circle cx="228" cy="95" r="1.2"/>
    </g>
    <polygon points="131,59 155,16 203,16 227,59 203,102 155,102" fill="#fff" stroke="var(--blue)" stroke-width="4"/>
    <polygon points="138,59 159,22 199,22 220,59 199,96 159,96" fill="#fff" stroke="var(--navy)" stroke-width=".5"/>
    <g font-family="Poppins, sans-serif" font-size="7.2" font-weight="600" fill="var(--navy)" text-anchor="middle">
      <text x="179" y="45">WE HELP</text><text x="179" y="56">COMPANIES</text><text x="179" y="67">INCREASE</text><text x="179" y="78">VALUATION BY</text>
    </g>
  </svg>

  <p class="copy" style="left:20px;top:234px;width:316px">HarborLeap provides executives and business owners with clear guidance to unlock value ahead of an exit. Our non-disruptive, ala-carte process enables us to work with sellers on specific areas or to do a complete analysis and recommendation and can include:</p>
  <div class="tab" style="top:261px;width:140px;padding-left:10px">BRAND ANALYSIS AND RECOMMENDATIONS</div>
  <p class="copy" style="left:20px;top:275px;width:316px">Strong brands command a higher valuation. We conduct a brand analysis, providing clear and detailed recommendations to enhance your value proposition and help you stand out from the crowd:</p>
  <ul class="bullets" style="left:20px;top:294px;width:316px">
    <li style="--c:var(--blue)"><span class="lead">Current external position among competitors</span> : We look at how your brand measures up based on external competitive analysis, positioning in the media and analyst community, and across other digital channels.</li>
    <li style="--c:var(--teal)"><span class="lead">Physical brand image</span> : A little bit of paint and updated fixtures can go a long way when increasing the value of a home. The same is true for businesses. Our audit evaluates non-disruptive steps your company can take to enhance your brand look and feel before sale.</li>
    <li style="--c:var(--red)"><span class="lead">Employee brand perception</span> : We conduct a high-level external audit with recommendations to enhance engagement for current and prospective employees.</li>
    <li style="--c:var(--orange)"><span class="lead">Customer brand perception</span> : We conduct a high-level external audit showcasing how customers perceive your brand in the market. We then provide recommendations for enhancing engagement and maximizing value.</li>
  </ul>

  <svg class="abs" style="left:0;top:420px" width="354" height="60" viewBox="0 0 354 60" fill="none" stroke="var(--navy)" stroke-width=".7">
    <polyline points="22,35 25,8 173,8"/>
    <polyline points="191,3 328,3 323,44"/>
    <polyline points="185,57 188,49"/>
  </svg>
  <p class="stat" style="left:28px;top:431px;width:145px">A <b>5%</b> increase in customer retention correlates with at least a <b>25%</b> increase in profit, according to an analysis by Halloway &amp; Company.</p>
  <p class="cite" style="left:24px;top:462px">(https://media.halloway.example/papers/retention_costs.pdf)</p>
  <p class="stat" style="left:191px;top:428px;width:128px;text-align:justify">It costs 5 times more to acquire a new customer than to retain a current one and <b>16</b> times more to get new customers to the same spending level as existing ones.</p>
  <p class="cite" style="left:190px;top:470px">(https://growthledger.example/customer-retention-guide-statistics/)</p>

  <div class="footer-bar"></div>
  <div class="footer-url">WWW.QUILLMARSH.PARTNERS.COM</div>
</section>

<section class="page page-3">
  <div class="tab" style="top:17px;width:229px">DIGITAL AND TRADITIONAL MARKETING ANALYSIS &amp; RECOMMENDATIONS</div>
  <p class="copy" style="left:18px;top:32px;width:309px;line-height:7.2px">How much money are you leaving on the table? Our marketing audits help organizations identify areas of hidden value that can have significant impacts on revenue and valuation. We optimize current activities and uncover new strategies to increase the effectiveness of current marketing spend. Areas we evaluate include:</p>
  <ul class="checks" style="left:19px;top:67px;width:210px">
    <li>Website traffic and conversion</li>
    <li>CRM process review to identify strategies and recommendations to increase conversion and reactive old-leads</li>
    <li>Email marketing strategy</li>
    <li>Automations and drip marketing</li>
    <li>Social media strategy /presence</li>
    <li>Partnership marketing</li>
    <li>Paid media analysis/strategy suggestion</li>
  </ul>
  <svg class="photo" style="left:243px;top:69px" width="111" height="88" viewBox="0 0 111 88" role="img" aria-label="Photograph of hands typing on a laptop showing a website">
    <defs>
      <linearGradient id="laptop" x1="0" y1="0" x2="1" y2="1">
        <stop offset="0" stop-color="#b9a691"/>
        <stop offset=".55" stop-color="#3b3f4a"/>
        <stop offset="1" stop-color="#d7d9de"/>
      </linearGradient>
    </defs>
    <polygon points="26,0 111,0 111,88 26,88 4,44" fill="url(#laptop)"/>
    <polyline points="22,0 0,44 22,88" fill="none" stroke="var(--teal)" stroke-width="3"/>
  </svg>

  <div class="tab" style="top:163px;width:199px">MESSAGING AND CONTENT STRATEGY REVIEW AND ANALYSIS</div>
  <p class="copy" style="left:19px;top:177px;width:309px">It's about your valuation. Full and fair valuation requires a clear, compelling investment case articulated consistently to the right audience at the right time. Messaging to maximize your value in an acquisition or an IPO is quite different from typical selling messages for prospects, customers, or 'features &amp; business benefits' for press and analysts. We understand the issues and speak the right language to maximize perception of value with key decision makers.</p>
  <ul class="dots" style="left:19px;top:225px;width:240px">
    <li>Review and recommendations of key messaging and value proposition.</li>
    <li>Analysis and recommendations to highlight data, IP, and innovation.</li>
    <li>Analysis and recommendations to position key executives likely to remain with the company as thought leaders to help build value.</li>
    <li>Analysis and recommendations to build employee engagement and retention enhancing your most valuable asset--your team.</li>
  </ul>

  <div class="tab" style="top:283px;width:160px">MEDIA AND ANALYST STRATEGY DEVELOPMENT</div>
  <p class="copy" style="left:18px;top:299px;width:309px">Positive articles and inclusion in analyst reports pack a powerful punch when preparing your business for sale. We work with clients to develop a media strategy that goes beyond brand awareness, leveraging media to build a digital history of third-party validation targeted to enhance appeal to prospective buyers while generating traffic and connections, to enhance overall value.</p>
  <p class="media-item" style="left:17px;top:344px">Positioning to media and analyst community creating third party validation .</p>
  <p class="media-item" style="left:17px;top:368px">Announcement timeline and strategy planning to maximize media value of news.</p>
  <p class="media-item" style="left:17px;top:393px">How to position that news for the most significant impact.</p>
  <p class="media-item" style="left:202px;top:345px">Key angle recommendations.</p>
  <p class="media-item" style="left:202px;top:368px">What is newsworthy.</p>

  <div class="review-box" style="left:25px;top:423px;width:302px;height:52px">
    <span class="review-title">WHITE HAT/BLACK HAT REVIEW</span>
    We take a buyer's communications and marketing approach to analyzing the client company and provide a "punch list" of things a potential buyer is likely to ask/request in due diligence from a comms/culture/marketing/reputation standpoint to ensure that when potential buyers start screening for sellers and evaluating them, the client company has the upper hand.
    <span class="stars">★★★★★</span>
  </div>

  <div class="footer-bar"></div>
  <div class="footer-url">WWW.QUILLMARSH.PARTNERS.COM</div>
</section>

<section class="page page-4">
  <div class="hero" style="height:136px"></div>
  <svg class="photo" width="354" height="136" viewBox="0 0 354 136" role="img" aria-label="Photograph of a whiteboard with sketched marketing diagrams">
    <defs>
      <linearGradient id="whiteboard" x1="0" y1="0" x2="1" y2="1">
        <stop offset="0" stop-color="#f2f2f0"/>
        <stop offset="1" stop-color="#d6d6d3"/>
      </linearGradient>
    </defs>
    <polygon points="223,0 354,0 354,136 187,136" fill="url(#whiteboard)"/>
  </svg>
  <div class="quote-frame" style="left:11px;top:35px;width:164px;height:74px"></div>
  <svg class="abs" style="left:62px;top:20px" width="52" height="34" viewBox="0 0 52 34">
    <rect x="0" y="0" width="52" height="22" fill="var(--navy)"/>
    <path d="M4 2h17v14l-6 14h-7l5-12H4z" fill="#fff"/>
    <path d="M28 2h17v14l-6 14h-7l5-12h-9z" fill="#fff"/>
  </svg>
  <p class="quote-line" style="left:14px;top:59px;width:158px">Strategy without tactics is the slowest route to victory. Tactics without strategy is the noise before defeat.</p>
  <p class="quote-by" style="left:11px;top:104px;width:164px"><span style="padding:0 4px;background:var(--navy)">– Wen Daoshi</span></p>

  <p class="copy" style="left:20px;top:147px;width:309px">Once the analysis is complete, we deliver actionable intelligence and recommendations to help leaders identify and quickly unlock areas that will boost value and appeal to prospective buyers. Work products include:</p>
  <span class="deliverable-icon" style="left:19px;top:184px"></span>
  <p class="deliverable" style="left:38px;top:183px;width:291px"><span class="lead">Gap Assessment</span> : We provide a comprehensive seller report providing analysis and actionable recommendations to increase your valuation while identifying and mitigating non-financial risks.</p>
  <span class="deliverable-icon" style="left:19px;top:209px"></span>
  <p class="deliverable" style="left:38px;top:208px;width:291px"><span class="lead">Strategic Roadmap</span> : Clients are given an actionable tactical roadmap based on the recommendation provided. Organizations can choose to implement key areas or include this powerful guide as part of their presentation to prospective buyers to highlight latent potential. The roadmap provides actionable steps buyers can take upon close as they make their case for your business with their investment committees.</p>
  <p class="copy" style="left:20px;top:257px;width:309px">Once the strategy integration roadmap is complete, your team can implement it on your timeline, we can work with your team providing guidance and executive-level support, or we can fully execute deliverables with our robust capabilities and team. : Clients are given an actionable tactical roadmap based on the recommendation provided. Organizations can choose to implement key areas or include this powerful guide as part of their presentation to prospective buyers to highlight latent potential. The roadmap provides actionable steps buyers can take upon close as they make their case for your business with their investment committees.</p>
  <p class="copy" style="left:20px;top:324px;width:309px">Our value proposition, based on delivering outcomes rather than just outputs, means that you receive the benefit and capability of deeply experienced corporate communications leaders without adding headcount or the time to identify, recruit, onboard and retain a new team member.</p>
  <p class="copy" style="left:20px;top:357px;width:309px">We help organizations enhance their valuation by identifying areas that will appeal most to buyers and ensuring those elements of your business are visible and memorable to those who matter most.</p>
  <p class="copy" style="left:20px;top:383px;width:309px">HarborLeap helps sellers maximize valuation and unlock hidden potential ahead of an exit - ensuring money is not left on the table.</p>

  <div class="brand-dark" style="left:103px;top:444px;width:158px">
    <span class="name">QUILLMARSH</span>
    <span class="sub">PARTNERS</span>
  </div>

  <div class="footer-bar"></div>
  <div class="footer-url">WWW.QUILLMARSH.PARTNERS.COM</div>
</section>

</body>
</html>
```